Aerospace Private Equity Firm Needs Website

We need a website for new private equity fund called Orlin Partners. We buy smaller companies in the aerospace and industrial industries. I have attached some information about the firm. An example of a site we like that is a similar business but focused in a different sector is www.travomedic.com. www.quarnestgrove.com is a firm that also invests in aerospace companies.

Industry/Entity Type

Equity

Number of Pages Required

1 page

Colors
0555a3
33a6d7
ec1f27

```html
<!DOCTYPE html>
<html lang="en">
<head>
<meta charset="utf-8">
<title>Orlin Partners – Executive Advisors</title>
<link href="https://fonts.googleapis.com/css2?family=Questrial&family=Lato:wght@400;700&display=swap" rel="stylesheet">
<style>
:root{
  --blue:#0a3f8f;
  --nav-blue:#0d3e8c;
  --red:#d01a20;
  --ink:#1b1b1b;
  --muted:#444;
  --rule:#d9d9d9;
  --footer:#050505;
}
*{margin:0;padding:0;box-sizing:border-box}
html,body{width:960px;height:1200px;overflow:hidden;background:#fff}
body{position:relative;font-family:'Lato',sans-serif;color:var(--ink)}
.hero{position:absolute;left:0;top:73px;width:960px;height:294px;
  background:radial-gradient(ellipse at 25% 10%,#fbd2a8 0%,#f6a867 35%,#e9783c 65%,#b85a3c 100%)}
.hero-sky{position:absolute;inset:0;background:linear-gradient(100deg,rgba(255,255,255,0) 55%,rgba(90,70,100,.35) 100%)}
.header-shape{position:absolute;left:0;top:0;width:960px;height:84px}
.brand{position:absolute;left:66px;top:22px;display:flex;align-items:center;gap:8px;
  font-family:'Questrial',sans-serif;font-size:26px;color:var(--nav-blue);letter-spacing:.5px}
.brand-dot{width:12px;height:12px;border-radius:50%;background:var(--red)}
.nav a{position:absolute;top:41px;font-family:'Questrial',sans-serif;font-size:14.5px;color:#fff;text-decoration:none;letter-spacing:.3px}
.nav .sep{position:absolute;top:45px;width:1px;height:12px;background:rgba(255,255,255,.25)}
.dropdown{position:absolute;left:364px;top:73px;width:148px;height:97px;background:rgba(255,240,230,.72)}
.dropdown a{display:block;height:21px;line-height:21px;margin:0 0 0 0;padding-left:14px;font-family:'Questrial',sans-serif;font-size:12px;color:#333;text-decoration:none;border-bottom:1px solid rgba(255,255,255,.7);letter-spacing:.3px}
.dropdown a:first-child{margin-top:2px}
.dropdown a.active{color:var(--red)}
.title{position:absolute;top:396px;width:960px;text-align:center;font-family:'Questrial',sans-serif;font-size:30px;color:var(--nav-blue);letter-spacing:.5px}
.title span{color:var(--red)}
.lede{position:absolute;top:448px;left:140px;width:680px;text-align:center;font-weight:700;font-size:14px;line-height:23px}
.advisor{position:absolute;top:519px;width:240px;text-align:center}
.avatar{width:92px;height:92px;margin:0 auto;border-radius:50%;border:2px solid #d8d8d8;background:radial-gradient(circle at 50% 40%,#e1b48a 0%,#c98f5d 45%,#f4f4f4 46%,#fff 100%)}
.advisor-name{margin-top:8px;font-family:'Questrial',sans-serif;font-size:15px;letter-spacing:.4px;color:var(--nav-blue)}
.advisor-name.active{color:var(--red)}
.bio{position:absolute;left:64px;top:674px;width:832px;height:432px;border:1px solid var(--rule);background:#fff;box-shadow:0 0 4px rgba(0,0,0,.06);padding:24px 34px 0 34px}
.bio-notch{position:absolute;left:591px;top:-11px;width:20px;height:20px;background:#fff;border-left:1px solid var(--rule);border-top:1px solid var(--rule);transform:rotate(45deg)}
.bio h2{font-size:13px;font-weight:700;color:var(--nav-blue);margin-bottom:9px}
.bio ul{list-style:none}
.bio>ul>li{font-size:11.5px;line-height:15px;padding-left:9px;text-indent:-9px;margin-bottom:10px;color:var(--ink)}
.bio li::before{content:"• ";}
.bio ul ul{margin-top:6px;padding-left:20px}
.bio ul ul li{font-size:9.5px;line-height:19.2px;text-indent:-7px;padding-left:7px;margin:0}
.footer{position:absolute;left:0;top:1160px;width:960px;height:40px;background:var(--footer);color:#e8e8e8;font-size:11.5px}
.footer p{position:absolute;left:65px;top:13px}
.social{position:absolute;top:7px;width:27px;height:27px;border-radius:50%;background:var(--nav-blue);border:2px solid #bcc8e0}
</style>
</head>
<body>
<div class="hero" role="img" aria-label="Passenger jet climbing through an orange sunset sky"><div class="hero-sky"></div></div>

<svg class="header-shape" viewBox="0 0 960 84" aria-hidden="true">
  <path d="M0 0 L960 0 L960 28 L292 28 C272 28 262 40 252 55 C244 68 236 83 220 83 L0 83 Z" fill="#fff"/>
  <path d="M292 28 L960 28 L960 73 L240 73 C246 66 248 62 252 55 C262 40 272 28 292 28 Z" fill="var(--nav-blue)"/>
  <path d="M0 83 L220 83 C236 83 244 68 252 55 C262 40 272 28 292 28" fill="none" stroke="var(--red)" stroke-width="1.5"/>
</svg>

<div class="brand"><span>Orlin Partners</span><span class="brand-dot"></span></div>

<nav class="nav">
  <a href="#" style="left:301px">Home</a><span class="sep" style="left:348px"></span>
  <a href="#" style="left:362px">Team</a><span class="sep" style="left:408px"></span>
  <a href="#" style="left:420px">Investment Strategy</a><span class="sep" style="left:558px"></span>
  <a href="#" style="left:570px">Portfolio Companies</a><span class="sep" style="left:714px"></span>
  <a href="#" style="left:726px">Press Releases</a><span class="sep" style="left:831px"></span>
  <a href="#" style="left:843px">Contact</a>
</nav>

<div class="dropdown">
  <a href="#">Our Team</a>
  <a href="#">Operating Partners</a>
  <a href="#" class="active">Executive Advisors</a>
  <a href="#">Our Partners</a>
</div>

<h1 class="title">Executive <span>Advisors</span></h1>
<p class="lede">Identify opportunities, assist with due diligence, serve on boards and mentor management –will have co-invest rights and share in the carry</p>

<div class="advisor" style="left:248px">
  <div class="avatar" role="img" aria-label="Advisor portrait placeholder"></div>
  <div class="advisor-name">Walter James (Jim) Hallcroft</div>
</div>
<div class="advisor" style="left:485px">
  <div class="avatar" role="img" aria-label="Advisor portrait placeholder"></div>
  <div class="advisor-name active">Dylan Marsh</div>
</div>

<section class="bio">
  <div class="bio-notch"></div>
  <h2>Two decades of investment banking experience focused on the aerospace and defense sectors</h2>
  <ul>
    <li>Managing Director in Brennard Hale’s Aerospace Defense Government (ADG) Group, based in LA</li>
    <li>Expertise in sell - side and buy - side M&amp;A advisory and complex corporate divestitures</li>
    <li>Advised industry leaders: Skyvane Co. and Westmark Aerodyne Corp., mid - cap publicly traded corporations, private equity investors, and privately - held, entrepreneurially operated businesses</li>
    <li>Sector expertise across multiple verticals including metallic and composite fabrication, engines and aerostructures, repair and maintenance, avionics, fasteners, and distribution</li>
    <li>Representative transactions, among others:
      <ul>
        <li>Sales of AirFlux; Corvent Fluid Systems to Vectrion</li>
        <li>Sales of Keystone Metalworks; Ridgeline Machine; Bexley Laser Works; and National Forgecraft to Aurel Castings</li>
        <li>Sale of Tarn Composites to Holloway plc</li>
        <li>Sale of Penrose Aerospace to Kestrin</li>
        <li>Sale of LMC Manufacturing to Granthorn</li>
        <li>Sale of Delvo to Lumetra</li>
        <li>Sale of Aerolink to Halvern</li>
      </ul>
    </li>
    <li>Prior to Brennard Hale – served as Director in the aerospace &amp; defense group at Marchand Frères; several years at Whitcombe &amp; Company; began career at Fieldgate Investment Partners</li>
    <li>BA in Economics from Western State University</li>
  </ul>
</section>

<footer class="footer">
  <p>Copyright © 2017 Orlin Partners.&nbsp;&nbsp; All Rights Reserved.</p>
  <span class="social" style="left:795px" aria-label="Social link"></span>
  <span class="social" style="left:831px" aria-label="Social link"></span>
  <span class="social" style="left:867px" aria-label="Social link"></span>
</footer>
</body>
</html>
```